Design professional, clean and neat beauty clinic

design an instagram style flyer similar style but have my own branding. Like they have their own. Must look different but also similar/better in professionalism. source file also needed.

Font styles to use
Sans Serif

```html
<!DOCTYPE html>
<html lang="en">
<head>
<meta charset="UTF-8">
<title>Lumera Clinic – Beauty Therapy Training Course</title>
<link href="https://fonts.googleapis.com/css2?family=Roboto:wght@400;500;700&display=swap" rel="stylesheet">
<style>
  :root {
    --teal: #00a99d;
    --ink: #1f1f1f;
    --slate: #4a4a4a;
    --white: #ffffff;
    --panel: #e8e8e8;
    --skin-light: #f3ddd2;
    --skin-mid: #e3bca8;
    --skin-deep: #c8947e;
  }
  * { margin: 0; padding: 0; box-sizing: border-box; }
  html, body { width: 1200px; height: 1200px; overflow: hidden; background: var(--white); }
  body { font-family: "Roboto", sans-serif; }

  .flyer { position: relative; width: 1200px; height: 1200px; background: var(--white); overflow: hidden; }

  .teal-band { position: absolute; left: 0; top: 628px; width: 1200px; height: 450px; background: var(--teal); }
  .teal-rule { position: absolute; left: 951px; top: 59px; width: 11px; height: 580px; background: var(--teal); }

  .portrait {
    position: absolute; left: 534px; top: 59px; width: 417px; height: 739px;
    background: linear-gradient(160deg, var(--skin-light) 0%, var(--skin-mid) 55%, var(--skin-deep) 100%);
  }

  .frame-line { position: absolute; background: var(--teal); }
  .frame-line.horizontal { left: 383px; top: 486px; width: 362px; height: 7px; }
  .frame-line.vertical { left: 738px; top: 486px; width: 7px; height: 312px; }

  .brand { position: absolute; left: 30px; top: 89px; display: flex; align-items: center; gap: 15px; z-index: 2; }
  .brand-dot { width: 82px; height: 82px; border-radius: 50%; background: var(--teal); }
  .brand-name { color: var(--teal); font-size: 25px; font-weight: 500; letter-spacing: 1.5px; }

  .headline { position: absolute; left: 44px; top: 216px; text-transform: uppercase; font-weight: 500; line-height: 1; z-index: 2; }
  .headline-top { display: block; color: var(--teal); font-size: 116px; letter-spacing: 1px; }
  .headline-bottom { display: block; color: var(--slate); font-size: 116px; margin-top: -8px; letter-spacing: 0; }

  .course { position: absolute; left: 52px; top: 486px; text-transform: uppercase; line-height: 1; z-index: 2; }
  .course-length { display: block; color: var(--teal); font-size: 48px; font-weight: 500; letter-spacing: 3px; }
  .course-name { display: block; color: var(--slate); font-size: 48px; font-weight: 400; letter-spacing: 1.5px; margin-top: 16px; }

  .offer {
    position: absolute; left: 810px; top: 254px; width: 522px; height: 158px;
    transform: rotate(90deg); transform-origin: center;
    color: var(--teal); font-size: 220px; font-weight: 700; line-height: 158px;
    text-align: center; letter-spacing: 4px;
  }

  .tagline { position: absolute; left: 53px; top: 690px; color: var(--white); font-size: 47px; font-weight: 700; line-height: 58px; text-transform: uppercase; }

  .intro { position: absolute; left: 49px; top: 833px; width: 1120px; color: var(--white); font-size: 30px; line-height: 47px; font-weight: 400; }

  .booking {
    position: absolute; left: 607px; top: 980px; width: 571px; height: 196px;
    background: var(--panel); border: 8px solid var(--white);
    display: flex; align-items: center; padding-left: 34px;
  }
  .booking-icon { width: 98px; height: 100px; flex: none; }
  .booking-text { margin-left: 30px; }
  .booking-label { color: var(--teal); font-size: 27px; font-weight: 500; letter-spacing: 2px; line-height: 1; }
  .booking-phone { color: var(--ink); font-size: 52px; font-weight: 700; line-height: 1; margin-top: 12px; letter-spacing: 1px; }

  .website { position: absolute; left: 47px; top: 1108px; color: var(--ink); font-size: 36px; font-weight: 500; letter-spacing: 2px; line-height: 1; }
</style>
</head>
<body>
  <main class="flyer">
    <div class="teal-band"></div>
    <div class="teal-rule"></div>

    <div class="portrait" role="img" aria-label="Close-up beauty portrait of a woman with closed eyes and soft makeup"></div>

    <div class="frame-line horizontal"></div>
    <div class="frame-line vertical"></div>

    <div class="brand">
      <span class="brand-dot"></span>
      <span class="brand-name">LUMERA CLINIC</span>
    </div>

    <h1 class="headline">
      <span class="headline-top">Beauty</span>
      <span class="headline-bottom">Therapy</span>
    </h1>

    <p class="course">
      <span class="course-length">6 Weeks</span>
      <span class="course-name">Training Course</span>
    </p>

    <div class="offer">FREE</div>

    <h2 class="tagline">The best beauty<br>session!</h2>

    <p class="intro">Your Beauty Session. Being a woman is all about being and feeling beauti-<br>ful. This is why we wear makeup and frequent the salon. It's why we dress<br>up when we</p>

    <div class="booking">
      <svg class="booking-icon" viewBox="0 0 98 100" aria-hidden="true">
        <path d="M14 4 L30 4 L38 26 L28 36 Q38 58 60 70 L70 60 L92 68 L92 84 Q90 96 76 96 Q40 92 18 68 Q2 46 2 18 Q4 6 14 4 Z" fill="#00a99d"/>
        <path d="M58 30 A12 12 0 0 1 70 42" fill="none" stroke="#00a99d" stroke-width="6" stroke-linecap="round"/>
        <path d="M58 16 A26 26 0 0 1 84 42" fill="none" stroke="#00a99d" stroke-width="6" stroke-linecap="round"/>
        <path d="M58 3 A39 39 0 0 1 96 42" fill="none" stroke="#00a99d" stroke-width="6" stroke-linecap="round"/>
      </svg>
      <div class="booking-text">
        <div class="booking-label">BOOK NOW</div>
        <div class="booking-phone">+96 555 0147</div>
      </div>
    </div>

    <div class="website">WWW.LUMERACLINIC.COM</div>
  </main>
</body>
</html>
```